Managed Service provider for IT support needs a three panel fold flyer

We are a Information & Technology company, providing compelte managed services ot the SMB market in southern Califonia.
Looking for a three panel, tri-fold or other, 3.75 X 8.35 Vertical flyer.
The final design should communicate a partnered techjnology solution

Managed Services:
Designed to reduce your costs, increase your profits and mitigate your business risks, we partner with you as your Virtual IT Department, allowing you to focus on running your business, not your technology.

https://brixolane.com/

It Company

```html
<!DOCTYPE html>
<html lang="en">
<head>
<meta charset="utf-8">
<title>Brixolane – Some of our Services</title>
<link href="https://fonts.googleapis.com/css2?family=Open+Sans:wght@400;600;700&display=swap" rel="stylesheet">
<style>
  :root {
    --stage: #2a2a2c;
    --blue-bar: #1a6fc0;
    --blue-bright: #1a86e0;
    --charcoal: #333436;
    --green: #7ed321;
    --white: #ffffff;
    --text-soft: #e8eef7;
  }
  * { box-sizing: border-box; margin: 0; padding: 0; }
  html, body { width: 1200px; height: 900px; overflow: hidden; }
  body {
    background: var(--stage);
    font-family: "Open Sans", Arial, sans-serif;
    color: var(--white);
    position: relative;
  }
  .flyer {
    position: absolute;
    left: 115px; top: 92px;
    width: 970px; height: 718px;
    overflow: hidden;
    box-shadow: 0 10px 30px rgba(0,0,0,.5);
  }
  .hero-photo {
    position: absolute; inset: 0;
    background:
      radial-gradient(ellipse 320px 380px at 820px 360px, rgba(10,20,40,.95), rgba(10,20,40,0) 70%),
      radial-gradient(ellipse 420px 300px at 430px 230px, #1f5db8 0%, rgba(31,93,184,0) 75%),
      linear-gradient(90deg, #0d3f8f 0%, #0a2e6c 45%, #081a3d 75%, #050d20 100%);
  }
  .panels { position: absolute; inset: 0; display: flex; }
  .panel {
    position: relative;
    width: 323.33px; height: 100%;
    border-right: 1px solid rgba(255,255,255,.08);
  }
  .panel:last-child { border-right: 0; }
  .panel-tab {
    position: absolute; left: 30px; top: 0;
    width: 265px; height: 48px;
    background: var(--green);
    font-size: 22px; font-weight: 600;
    line-height: 52px; text-align: center;
  }
  .service {
    position: absolute; left: 0; width: 100%;
    text-align: center;
  }
  .service--upper { top: 71px; }
  .service--lower { top: 368px; }
  .service-icon { display: block; margin: 0 auto; width: 64px; height: 72px; }
  .service-title {
    margin-top: 14px;
    font-size: 20px; font-weight: 600; line-height: 26px;
  }
  .service-rule {
    position: relative;
    width: 232px; height: 2px; margin: 8px auto 0;
    background: var(--green);
  }
  .service-rule::after {
    content: ""; position: absolute; left: 50%; top: 2px;
    margin-left: -4px;
    border-left: 4px solid transparent; border-right: 4px solid transparent;
    border-top: 4px solid var(--green);
  }
  .service-copy {
    margin: 15px auto 0; width: 244px;
    font-size: 12.2px; line-height: 16.3px;
    color: var(--text-soft);
  }
  .panel-footer {
    position: absolute; left: 0; bottom: 0;
    width: 100%; height: 43px;
    display: flex; align-items: center; justify-content: center; gap: 9px;
    font-size: 19px; line-height: 1;
  }
  .panel-footer svg { width: 15px; height: 15px; }
  .panel-footer--blue { background: var(--blue-bar); }
  .panel-footer--dark { background: var(--charcoal); border-top: 4px solid var(--white); height: 47px; }
  .panel-footer--bright { background: var(--blue-bright); }
  .panel-footer a { color: var(--white); text-decoration: none; }
</style>
</head>
<body>
<svg width="0" height="0" style="position:absolute">
  <defs>
    <symbol id="hex" viewBox="0 0 64 72">
      <polygon points="32,2 62,19 62,53 32,70 2,53 2,19" fill="#061633" stroke="#7ed321" stroke-width="1.6"/>
    </symbol>
    <symbol id="web" viewBox="0 0 16 16">
      <g fill="none" stroke="#fff" stroke-width="1.2">
        <circle cx="8" cy="8" r="6.5"/><ellipse cx="8" cy="8" rx="3" ry="6.5"/>
        <line x1="1.5" y1="8" x2="14.5" y2="8"/>
      </g>
    </symbol>
  </defs>
</svg>

<main class="flyer">
  <div class="hero-photo" role="img" aria-label="Blurred photo of a businessman touching a glowing network of connected user icons"></div>

  <div class="panels">
    <section class="panel">
      <h2 class="panel-tab">Some of our Services</h2>

      <article class="service service--upper">
        <svg class="service-icon" viewBox="0 0 64 72" aria-hidden="true">
          <use href="#hex"/>
          <circle cx="32" cy="36" r="14" fill="#fff"/>
          <path d="M24 28c4 1 5 4 3 6s2 5 0 8M36 24c-2 3 1 5 4 5s3 4 1 6M38 44c-2-2 0-5 3-4" fill="none" stroke="#061633" stroke-width="2.4"/>
        </svg>
        <h3 class="service-title">Managed IT Services</h3>
        <div class="service-rule"></div>
        <p class="service-copy">We deliver proactive flat-rate Managed IT Services in Larkmont, CA . Designed to reduce your costs, eliminate business pain, increase your profits and mitigate business risks, we partner with you as your Virtual IT Department and outsourced CTO, allowing you to focus on running your business, not your technology.</p>
      </article>

      <article class="service service--lower">
        <svg class="service-icon" viewBox="0 0 64 72" aria-hidden="true">
          <use href="#hex"/>
          <rect x="27" y="23" width="10" height="6" rx="1.5" fill="none" stroke="#fff" stroke-width="2.2"/>
          <rect x="18" y="28" width="28" height="20" rx="3" fill="#fff"/>
          <rect x="30" y="31" width="4" height="14" fill="#061633"/>
          <rect x="25" y="36" width="14" height="4" fill="#061633"/>
        </svg>
        <h3 class="service-title">Healthcare IT Services</h3>
        <div class="service-rule"></div>
        <p class="service-copy">Do you need a HIPAA and HiTech-compliant Healthcare IT Service Provider? Does your practice require expert EMR and Practice Management Software support? Would you like to reduce the cost and complexity of your technology? Our Healthcare Technology Solutions in Larkmont, CA are the answer.</p>
      </article>

      <footer class="panel-footer panel-footer--blue">
        <svg aria-hidden="true"><use href="#web"/></svg>
        <a href="https://brixolane.com/">www.brixolane.com</a>
      </footer>
    </section>

    <section class="panel">
      <h2 class="panel-tab">Some of our Services</h2>

      <article class="service service--upper">
        <svg class="service-icon" viewBox="0 0 64 72" aria-hidden="true">
          <use href="#hex"/>
          <path d="M44 22c-8 0-15 5-18 13l5 5c8-3 13-10 13-18z" fill="#fff"/>
          <circle cx="37" cy="30" r="2.6" fill="#061633"/>
          <path d="M27 33l-6 1-3 4 7-1zM33 41l-1 6-4 3 1-7z" fill="#fff"/>
          <path d="M24 42c-3 1-4 4-5 8 4-1 7-2 8-5z" fill="#fff"/>
        </svg>
        <h3 class="service-title">Engineering IT Services</h3>
        <div class="service-rule"></div>
        <p class="service-copy">Are you seeking an IT firm experienced in supporting your Engineering processes, equipment and software applications? Would you like to reduce the cost and complexity of your technology and increase uptime? We deliver complete Engineering Technology Solutions in Larkmont, CA .</p>
      </article>

      <article class="service service--lower">
        <svg class="service-icon" viewBox="0 0 64 72" aria-hidden="true">
          <use href="#hex"/>
          <g fill="none" stroke="#fff">
            <circle cx="27" cy="39" r="8" stroke-width="5" stroke-dasharray="3.2 2.1"/>
            <circle cx="27" cy="39" r="3" stroke-width="2"/>
            <circle cx="39" cy="29" r="5" stroke-width="3.5" stroke-dasharray="2.2 1.6"/>
            <circle cx="40" cy="46" r="4.5" stroke-width="3.2" stroke-dasharray="2 1.5"/>
          </g>
        </svg>
        <h3 class="service-title">Manufacturing IT Services</h3>
        <div class="service-rule"></div>
        <p class="service-copy">Do you need an IT firm experienced in supporting your manufacturing processes, equipment and specialized line of business applications? Our manufacturing IT services in Larkmont, CA include remote and onsite system and software support, 24×7 network monitoring, patching and updating and more.</p>
      </article>

      <footer class="panel-footer panel-footer--dark">
        <svg aria-hidden="true"><use href="#web"/></svg>
        <a href="https://brixolane.com/">www.brixolane.com</a>
      </footer>
    </section>

    <section class="panel">
      <h2 class="panel-tab">Some of our Services</h2>

      <article class="service service--upper">
        <svg class="service-icon" viewBox="0 0 64 72" aria-hidden="true">
          <use href="#hex"/>
          <rect x="22" y="22" width="20" height="28" rx="2" fill="#fff"/>
          <rect x="25" y="25" width="14" height="6" fill="#061633"/>
          <g fill="#061633">
            <rect x="25" y="34" width="3.5" height="3"/><rect x="30.3" y="34" width="3.5" height="3"/><rect x="35.5" y="34" width="3.5" height="3"/>
            <rect x="25" y="39" width="3.5" height="3"/><rect x="30.3" y="39" width="3.5" height="3"/><rect x="35.5" y="39" width="3.5" height="3"/>
            <rect x="25" y="44" width="3.5" height="3"/><rect x="30.3" y="44" width="3.5" height="3"/><rect x="35.5" y="44" width="3.5" height="3"/>
          </g>
        </svg>
        <h3 class="service-title">Accounting IT Services</h3>
        <div class="service-rule"></div>
        <p class="service-copy">Are you seeking an IT firm experienced in supporting the multiple versions of your Accounting Practice’s specific line of business software applications? Would you like to increase the security and availability of your network? Our Accounting Technology Solutions in Larkmont, CA are the answer.</p>
      </article>

      <article class="service service--lower">
        <svg class="service-icon" viewBox="0 0 64 72" aria-hidden="true">
          <use href="#hex"/>
          <g fill="none" stroke="#fff" stroke-width="1.8">
            <line x1="32" y1="22" x2="32" y2="48"/>
            <line x1="20" y1="27" x2="44" y2="27"/>
            <path d="M20 27l-5 11M20 27l5 11M44 27l-5 11M44 27l5 11"/>
          </g>
          <path d="M14 38h12a6 4 0 0 1-12 0zM38 38h12a6 4 0 0 1-12 0z" fill="#fff"/>
          <rect x="25" y="48" width="14" height="3" fill="#fff"/>
          <circle cx="32" cy="22" r="2" fill="#fff"/>
        </svg>
        <h3 class="service-title">Legal IT Services</h3>
        <div class="service-rule"></div>
        <p class="service-copy">Do you need an IT firm versed in supporting your legal processes and applications, e-discovery, archiving and secure document management? Increase the security and availability of your critical data, systems and services with our Legal Technology Solutions in Larkmont, CA .</p>
      </article>

      <footer class="panel-footer panel-footer--bright">
        <svg aria-hidden="true"><use href="#web"/></svg>
        <a href="https://brixolane.com/">www.brixolane.com</a>
      </footer>
    </section>
  </div>
</main>
</body>
</html>
```